Business Card Design

I am an child sleep consultant. I would like the picture to be the background of the card and for my logo to be in the upper right hand corner. Other than that, the design is yours!!

Business

Marta Kovel
Red Fern Slumber
Certified Child Sleep Consultant
(555) 286-9153
redfernslumber.com

```html
<!DOCTYPE html>
<html lang="en">
<head>
<meta charset="utf-8">
<title>Red Fern Slumber – Business Card</title>
<link rel="stylesheet" href="https://fonts.googleapis.com/css2?family=Tinos&family=Michroma&family=Ubuntu:wght@400;500&display=swap">
<style>
  :root {
    --panel-dark: #2b1a17;
    --panel-mid: #3a211b;
    --photo-light: #d9c4bd;
    --photo-mid: #a77a6c;
    --photo-dark: #4a2a22;
    --band: rgba(235, 222, 216, 0.45);
    --ink: #111111;
    --white: #ffffff;
    --chip: rgba(255, 255, 255, 0.28);
  }
  html, body {
    margin: 0;
    padding: 0;
    width: 1200px;
    height: 720px;
    overflow: hidden;
    background: #ffffff;
  }
  .card {
    position: relative;
    width: 1200px;
    height: 720px;
    overflow: hidden;
    background:
      radial-gradient(ellipse at 95% 80%, rgba(181, 67, 42, 0.35), transparent 45%),
      linear-gradient(180deg, var(--panel-mid), var(--panel-dark));
  }
  .card-photo {
    position: absolute;
    left: 0;
    top: 0;
    width: 763px;
    height: 720px;
    background:
      radial-gradient(ellipse at 22% 45%, var(--photo-light) 0%, var(--photo-mid) 45%, transparent 75%),
      linear-gradient(160deg, var(--photo-mid) 0%, var(--photo-dark) 60%, #2a1712 100%);
  }
  .identity-band {
    position: absolute;
    left: 43px;
    top: 366px;
    width: 660px;
    height: 64px;
    background: linear-gradient(90deg, transparent, var(--band) 15%, var(--band) 85%, transparent);
  }
  .identity-line {
    position: absolute;
    left: 23px;
    width: 700px;
    margin: 0;
    text-align: center;
    line-height: 1;
    white-space: nowrap;
  }
  .person-name {
    top: 233px;
    font-family: "Tinos", "Times New Roman", serif;
    font-weight: 400;
    font-size: 56px;
    color: var(--white);
    text-shadow: 0 2px 3px rgba(0, 0, 0, 0.5);
  }
  .business-name {
    top: 302px;
    font-family: "Michroma", "Arial", sans-serif;
    font-variant: small-caps;
    font-size: 52px;
    letter-spacing: 3px;
    color: var(--white);
    text-shadow: 2px 2px 3px rgba(0, 0, 0, 0.85);
  }
  .job-title {
    top: 374px;
    font-family: "Tinos", "Times New Roman", serif;
    font-size: 42px;
    color: var(--ink);
  }
  .identity-rule {
    position: absolute;
    left: 120px;
    top: 436px;
    width: 500px;
    height: 1px;
    background: linear-gradient(90deg, transparent, rgba(255, 255, 255, 0.6), transparent);
  }
  .contact-list {
    position: absolute;
    left: 775px;
    top: 238px;
    margin: 0;
    padding: 0;
    list-style: none;
    font-family: "Ubuntu", "Helvetica", sans-serif;
    font-size: 28px;
    line-height: 37px;
    color: var(--white);
  }
  .contact-item {
    display: flex;
    align-items: flex-start;
    margin-bottom: 24px;
  }
  .contact-icon {
    flex: none;
    width: 32px;
    height: 32px;
    margin-right: 30px;
    margin-top: 2px;
    background: var(--chip);
    border-radius: 2px;
    display: flex;
    align-items: center;
    justify-content: center;
  }
  .social-list {
    position: absolute;
    left: 775px;
    top: 548px;
    margin: 0;
    padding: 0;
    list-style: none;
  }
  .social-dot {
    width: 34px;
    height: 34px;
    margin-bottom: 18px;
    border-radius: 50%;
    background: var(--white);
  }
  .brand-mark {
    position: absolute;
    right: 24px;
    top: 34px;
    display: flex;
    align-items: center;
    gap: 10px;
    font-family: "Ubuntu", "Helvetica", sans-serif;
    font-weight: 500;
    font-size: 22px;
    line-height: 1.1;
    color: var(--white);
    text-align: left;
  }
  .brand-square {
    width: 28px;
    height: 28px;
    background: var(--white);
  }
</style>
</head>
<body>
  <main class="card">
    <div class="card-photo" role="img" aria-label="Background photograph of a baby in warm sepia tones"></div>

    <div class="brand-mark">
      <span class="brand-square"></span>
      <span class="brand-name">Red Fern<br>Slumber</span>
    </div>

    <div class="identity-band"></div>
    <h1 class="identity-line person-name">Marta Kovel</h1>
    <p class="identity-line business-name">Red Fern Slumber</p>
    <p class="identity-line job-title">Certified Child Sleep Consultant</p>
    <div class="identity-rule"></div>

    <ul class="contact-list">
      <li class="contact-item">
        <span class="contact-icon">
          <svg width="14" height="18" viewBox="0 0 14 18"><rect x="2" y="1" width="10" height="16" rx="1.5" fill="none" stroke="#fff" stroke-width="1.6"/><rect x="4" y="3.5" width="6" height="9" fill="#fff"/></svg>
        </span>
        <span>(555) 286-9153</span>
      </li>
      <li class="contact-item">
        <span class="contact-icon">
          <svg width="16" height="20" viewBox="0 0 16 20"><path d="M8 19 C8 19 2 11 2 7.5 A6 6 0 0 1 14 7.5 C14 11 8 19 8 19 Z" fill="none" stroke="#fff" stroke-width="1.6"/><circle cx="8" cy="7.5" r="2" fill="#fff"/></svg>
        </span>
        <span>123 First Street<br>New York, NY</span>
      </li>
      <li class="contact-item">
        <span class="contact-icon">
          <svg width="16" height="12" viewBox="0 0 16 12"><rect x="1" y="1" width="14" height="10" fill="none" stroke="#fff" stroke-width="1.5"/><path d="M1 1 L8 7 L15 1" fill="none" stroke="#fff" stroke-width="1.5"/></svg>
        </span>
        <span>redfernslumber.com</span>
      </li>
      <li class="contact-item">
        <span class="contact-icon">
          <svg width="16" height="16" viewBox="0 0 16 16"><circle cx="8" cy="8" r="6.5" fill="none" stroke="#fff" stroke-width="1.6"/><path d="M8 4 V8 L11 10" fill="none" stroke="#fff" stroke-width="1.6"/></svg>
        </span>
        <span>www.company.com</span>
      </li>
    </ul>

    <ul class="social-list">
      <li class="social-dot" aria-label="Social profile"></li>
      <li class="social-dot" aria-label="Social profile"></li>
    </ul>
  </main>
</body>
</html>
```